Sunny Paths and joy Business card

I have a logo, but will like a business card design. Is for a travel agency in Mexico. We focus in family experiences.

I will liek some thing different and unique, from the traditional business card, something to get remmeber for.

Business card information:

Leandro T. Ocampo
leandro@sunnypathsjoy.example

Alameda 482, 3 piso
Col. Tlalpizco
Mexico, D.F. 07320

office: (55) 5000-0142
mobile: (55) 9000-0187

www.sunnypathsjoy.example
@sunnypjoy
blog: sunnypathsandjoy.blogsite.example
facebook: SunnyPathsAndJoy

```html
<!DOCTYPE html>
<html lang="es">
<head>
<meta charset="utf-8">
<title>Sunny Paths and joy — Business card</title>
<link rel="stylesheet" href="https://fonts.googleapis.com/css2?family=Source+Serif+4:wght@400;700&display=swap">
<style>
  :root {
    --paper: #ffffff;
    --ink: #3a3a3a;
    --muted: #8a8a8a;
    --frame: #ffffff;
    --sky-top: #2f6fc4;
    --sky-mid: #8fb6e4;
    --sea: #4f9fbf;
    --sand: #e9e1d2;
    --sand-deep: #cfc3ad;
  }
  * { margin: 0; padding: 0; box-sizing: border-box; }
  html, body { width: 1200px; height: 336px; overflow: hidden; background: var(--paper); }
  body { font-family: "Source Serif 4", Georgia, serif; color: var(--ink); }

  .card-sheet { position: relative; width: 1200px; height: 336px; }

  .card-front {
    position: absolute; left: 0; top: 0; width: 560px; height: 336px;
    background: linear-gradient(180deg, var(--sky-top) 0%, var(--sky-mid) 38%, var(--sea) 50%, var(--sand) 62%, var(--sand-deep) 100%);
  }
  .name-frame {
    position: absolute; left: 54px; top: 44px; width: 124px; height: 86px;
    border: 1.5px solid var(--frame);
  }
  .front-name, .front-role {
    position: absolute; top: 82px; font-size: 14px; color: var(--frame); white-space: nowrap;
  }
  .front-name { left: 58px; }
  .front-role { left: 186px; }

  .card-back { position: absolute; left: 560px; top: 0; width: 640px; height: 336px; background: var(--paper); }
  .back-frame {
    position: absolute; left: 135px; top: 44px; width: 125px; height: 94px;
    background: linear-gradient(180deg, var(--sky-top) 0%, var(--sky-mid) 60%, #c9dbef 100%);
  }
  .back-name, .back-role { position: absolute; top: 82px; font-size: 14px; white-space: nowrap; }
  .back-name { left: 139px; color: var(--frame); }
  .back-role { left: 266px; color: var(--muted); }

  .contact-list {
    position: absolute; left: 365px; top: 198px; list-style: none;
    font-size: 12.5px; line-height: 16px; white-space: nowrap;
  }
  .contact-list b { font-weight: 700; margin-right: 4px; }
</style>
</head>
<body>
<main class="card-sheet">
  <section class="card-front">
    <div class="beach-photo" role="img" aria-label="Photo of a sunny beach with thatched palm umbrellas and white lounge chairs" style="position:absolute;inset:0;"></div>
    <div class="name-frame"></div>
    <p class="front-name">Leandro T. Ocampo</p>
    <p class="front-role">Travel Agent</p>
  </section>

  <section class="card-back">
    <div class="back-frame" role="img" aria-label="Cropped detail of the beach photo showing blue sky"></div>
    <p class="back-name">Leandro T. Ocampo</p>
    <p class="back-role">Travel Agent</p>
    <ul class="contact-list">
      <li>Alameda 482, 3 piso Col. Tlalpizco</li>
      <li>Mexico, D.F. 07320</li>
      <li><b>office</b>(55) 5000-0142</li>
      <li><b>mobile</b>(55) 9000-0187</li>
      <li><b>email</b>leandro@sunnypathsjoy.example</li>
      <li><b>site</b>www.sunnypathsjoy.example</li>
      <li><b>blog</b>sunnypathsandjoy.blogsite.example</li>
      <li><b>facebook</b>SunnyPathsAndJoy</li>
    </ul>
  </section>
</main>
</body>
</html>
```